Lime Wash Direct Mail Postcard Design

I need a postcard that is going to be mailed.
We are a residential and commerical painting company. We are going to start marking our Ventian Plaster, Lime Wash, Roman Clay, Mineral Wash.
I've attached the layout to use that shows bleed and such. I've included a mock up I've done to get an idea of what I want.
- I want it to look sophicated
- Speciality
- Art
I've included logos of 2 companies - Velastra and Cindrel to show.
I want to show mostly interior work but one or 2 lime wash houses that's lighter, shows the bricks in area would be good.
I love the saying "You're unique - Your Home Should Be Too" or if you have a better variation of that, I'd be open to it.

```html
<!DOCTYPE html>
<html lang="en">
<head>
<meta charset="utf-8">
<title>Halden Painting – Specialty Finishes Postcard</title>
<link rel="stylesheet" href="https://fonts.googleapis.com/css2?family=Anton&family=Archivo:wght@500;600;700&family=Cormorant+Garamond:wght@600&display=swap">
<style>
  :root {
    --page: #ffffff;
    --card: #ffffff;
    --panel-grey: #8a8a8a;
    --ink-white: #ffffff;
    --ink-dark: #262626;
    --gold: #ecd49a;
    --taupe: #9e8f87;
    --umber: #6f5039;
    --espresso: #4a413a;
    --frame: #453d36;
    --dot-grey: #c9cacc;
    --dot-black: #000000;
    --rule: #1a1a1a;
  }
  * { box-sizing: border-box; margin: 0; padding: 0; }
  html, body {
    width: 849px; height: 1200px; overflow: hidden;
    background: var(--page);
  }
  .sheet { position: relative; width: 849px; height: 1200px; }

  .postcard {
    position: absolute; left: 85px; width: 679px; height: 482px;
    background: var(--card);
    box-shadow: 0 3px 10px rgba(0,0,0,0.28);
  }
  .postcard--front { top: 67px; }
  .postcard--back { top: 651px; }

  .block { position: absolute; }

  /* front: finish swatches */
  .swatch-venetian { left: 48px; top: 49px; width: 164px; height: 163px;
    background: linear-gradient(135deg, #6b6b69 0%, #4c4c4a 40%, #7a7977 70%, #555553 100%); }
  .swatch-limewash-brick { left: 48px; top: 226px; width: 164px; height: 164px;
    background: linear-gradient(180deg, #ececec 0%, #e2e2e2 70%, #9a8a86 72%, #8a7f7c 100%); }
  .bar-umber { left: 48px; top: 403px; width: 164px; height: 31px; background: var(--umber); }

  .bar-taupe { left: 229px; top: 49px; width: 164px; height: 26px; background: var(--taupe); }
  .photo-exterior { left: 229px; top: 91px; width: 164px; height: 163px;
    background: linear-gradient(90deg, #a9c6de 0%, #7c9a5a 38%, #4a4846 40%, #6a6866 70%, #8d8b88 100%); }
  .swatch-roman-clay { left: 229px; top: 270px; width: 164px; height: 164px;
    background: linear-gradient(180deg, #e6e6e6 0%, #dcdcdc 85%, #d6ccbf 86%, #cfc3b4 100%); }

  .dot { position: absolute; border-radius: 50%; width: 42px; height: 42px; }
  .dot--grey { left: 108px; top: 198px; background: var(--dot-grey); }
  .dot--black { left: 290px; top: 241px; background: var(--dot-black); }

  .headline-panel {
    left: 410px; top: 49px; width: 221px; height: 385px;
    background: var(--panel-grey); color: var(--ink-white);
    text-align: center;
  }
  .headline {
    font-family: "Anton", "Arial Narrow", sans-serif;
    font-size: 86px; line-height: 0.9; letter-spacing: -1px;
    margin-top: 8px; text-transform: uppercase;
  }
  .subhead {
    font-family: "Archivo", Arial, sans-serif; font-weight: 600;
    font-size: 22px; line-height: 1.1; margin-top: 4px;
    text-transform: uppercase; letter-spacing: -0.3px;
  }
  .brand {
    display: flex; align-items: center; justify-content: center; gap: 7px;
    margin-top: 58px;
    font-family: "Archivo", Arial, sans-serif; font-weight: 700;
    font-size: 19px; color: var(--ink-dark); letter-spacing: 0.5px;
    text-transform: uppercase;
  }
  .brand__mark { width: 12px; height: 12px; background: var(--ink-dark); }
  .partners {
    position: absolute; left: 0; right: 0; bottom: 8px;
    display: flex; justify-content: space-between; padding: 0 12px;
    font-family: "Archivo", Arial, sans-serif; font-weight: 600;
    font-size: 16px; letter-spacing: 0.5px; text-transform: uppercase;
  }
  .partners__velastra { color: var(--ink-white); }
  .partners__cindrel { color: var(--gold); }

  /* back */
  .stamp-box { left: 524px; top: 40px; width: 103px; height: 106px; background: var(--espresso); }
  .address-line { position: absolute; left: 346px; width: 285px; height: 1px; background: var(--rule); }

  .snapshot {
    position: absolute; width: 183px; background: var(--frame);
    transform: translate(-50%, -50%) rotate(17.3deg);
    padding: 11px 11px 0;
  }
  .snapshot--tools { left: 149px; top: 130px; height: 173px; }
  .snapshot--brushes { left: 149px; top: 333px; height: 212px; }
  .snapshot__photo { width: 100%; border: 1px solid #cfcac4; }
  .snapshot--tools .snapshot__photo { height: 138px;
    background: linear-gradient(160deg, #e4e4e4 0%, #bdbdbd 45%, #c79a6a 70%, #e6d3b3 100%); }
  .snapshot--brushes .snapshot__photo { height 150px; height: 150px;
    background: linear-gradient(150deg, #6b4a33 0%, #3a2a20 40%, #b88a5c 65%, #4d3526 100%); }
  .snapshot__caption {
    font-family: "Cormorant Garamond", Georgia, serif; font-weight: 600;
    color: var(--ink-white); font-size: 11.5px; line-height: 1.05;
    text-align: center; text-transform: uppercase; margin-top: 6px;
  }
</style>
</head>
<body>
<main class="sheet">

  <section class="postcard postcard--front" aria-label="Postcard front">
    <div class="block swatch-venetian" role="img" aria-label="Dark grey Venetian plaster texture"></div>
    <div class="block swatch-limewash-brick" role="img" aria-label="White lime-washed brick wall with potted topiary on pastel wooden floor"></div>
    <div class="block bar-umber"></div>

    <div class="block bar-taupe"></div>
    <div class="block photo-exterior" role="img" aria-label="Pressure washer spraying a grey brick house exterior"></div>
    <div class="block swatch-roman-clay" role="img" aria-label="Pale grey Roman clay wall above light wood floor"></div>

    <span class="dot dot--grey"></span>
    <span class="dot dot--black"></span>

    <div class="block headline-panel">
      <h1 class="headline">You're<br>Unique</h1>
      <p class="subhead">Your home<br>should be too</p>
      <div class="brand"><span class="brand__mark"></span>Halden Painting</div>
      <div class="partners">
        <span class="partners__velastra">Velastra</span>
        <span class="partners__cindrel">Cindrel</span>
      </div>
    </div>
  </section>

  <section class="postcard postcard--back" aria-label="Postcard back">
    <figure class="snapshot snapshot--tools">
      <div class="snapshot__photo" role="img" aria-label="Plastering trowels and putty knives on a work surface"></div>
    </figure>
    <figure class="snapshot snapshot--brushes">
      <div class="snapshot__photo" role="img" aria-label="Paint brushes with wooden handles on a rustic table"></div>
      <figcaption class="snapshot__caption">You're unique<br>your home should be too</figcaption>
    </figure>

    <div class="block stamp-box"></div>

    <span class="address-line" style="top:224px"></span>
    <span class="address-line" style="top:261px"></span>
    <span class="address-line" style="top:295px"></span>
    <span class="address-line" style="top:330px"></span>
    <span class="address-line" style="top:363px"></span>
    <span class="address-line" style="top:397px"></span>
    <span class="address-line" style="top:432px"></span>
  </section>

</main>
</body>
</html>
```